Company Culture, Vision, Mission Posters for office

We are rebranding ourselves and have visuals we utilize in our offices that highlight our Mission, Vision, and Company Culture. These visuals will be utilized in posters in our offices, as 8.5" x 11" one-pagers as as trade show banners. I am including the current design, a word document with the content, and visuals of other marketing collateral we are designing.

Font styles to use
Sans Serif

Requirements
Must have
• Use Nexa Bold for headlines and Ebrima for content font

Our orange is CMYK: 2c, 66m, 87y, 0k
Our blue is CMYK: 84c, 69m, 47y, 39k

Culture version must utilize a pyramid to visualize how each pillar in our culture builds on each other.

```html
<!DOCTYPE html>
<html lang="en">
<head>
<meta charset="utf-8">
<title>Vantora Group – Core Values</title>
<link rel="stylesheet" href="https://fonts.googleapis.com/css2?family=Montserrat:wght@600;700&family=Mukta:wght@400&display=swap">
<style>
  :root {
    --orange: #f0773a;
    --navy: #2b3a4b;
    --mist: #e6e5e6;
    --paper: #ffffff;
    --backdrop: #d9d9db;
  }
  html, body {
    margin: 0;
    padding: 0;
    width: 1040px;
    height: 1200px;
    overflow: hidden;
    background: var(--backdrop);
  }
  .poster {
    position: absolute;
    left: 80px;
    top: 30px;
    width: 880px;
    height: 1139px;
    background: var(--paper);
    overflow: hidden;
    font-family: "Mukta", sans-serif;
    color: var(--navy);
  }
  .poster-shapes {
    position: absolute;
    inset: 0;
  }
  .brand {
    position: absolute;
    left: 459px;
    width: 400px;
    top: 34px;
    text-align: center;
  }
  .brand-dot {
    width: 72px;
    height: 72px;
    border-radius: 50%;
    background: var(--orange);
    margin: 0 auto 20px;
  }
  .brand-name {
    font-family: "Montserrat", sans-serif;
    font-weight: 700;
    font-size: 37px;
    letter-spacing: 0.1em;
    color: var(--navy);
    line-height: 1;
    white-space: nowrap;
  }
  .banner-title {
    position: absolute;
    left: 54px;
    top: 196px;
    margin: 0;
    font-family: "Montserrat", sans-serif;
    font-weight: 700;
    font-size: 38px;
    letter-spacing: -0.01em;
    color: #fff;
    line-height: 48px;
  }
  .intro {
    position: absolute;
    left: 84px;
    top: 305px;
    width: 760px;
    margin: 0;
    font-size: 23px;
    line-height: 28px;
  }
  .values {
    list-style: none;
    margin: 0;
    padding: 0;
  }
  .value {
    position: absolute;
    left: 0;
    width: 860px;
  }
  .value::before {
    content: "";
    position: absolute;
    left: 34px;
    top: 2px;
    width: 34px;
    height: 34px;
    border-radius: 50%;
    background: var(--orange);
  }
  .value-name {
    display: block;
    margin-left: 79px;
    font-family: "Montserrat", sans-serif;
    font-weight: 600;
    font-size: 22px;
    color: var(--orange);
    line-height: 38px;
  }
  .value-text {
    display: block;
    margin-left: 84px;
    width: 760px;
    font-size: 23px;
    line-height: 28px;
  }
  .value-integrity   { top: 409px; }
  .value-dedication  { top: 492px; }
  .value-reliability { top: 601px; }
  .value-value       { top: 712px; }
  .value-unity       { top: 823px; }
  .web-address {
    position: absolute;
    left: 258px;
    width: 622px;
    top: 1011px;
    height: 90px;
    line-height: 90px;
    text-align: center;
    font-family: "Montserrat", sans-serif;
    font-weight: 600;
    font-size: 21px;
    letter-spacing: 0.3em;
    color: #fff;
    text-indent: -40px;
  }
</style>
</head>
<body>
  <main class="poster">
    <svg class="poster-shapes" width="880" height="1139" viewBox="0 0 880 1139" aria-hidden="true">
      <rect class="header-band" x="0" y="0" width="880" height="215" fill="var(--mist)"/>
      <polygon class="header-stripe" points="0,154 275,154 291,173 0,173" fill="var(--navy)"/>
      <polygon class="header-banner" points="0,173 443,173 483,219 443,265 0,265" fill="var(--orange)"/>
      <rect class="footer-band" x="0" y="1053" width="880" height="86" fill="var(--mist)"/>
      <polygon class="footer-stripe" points="438,991 880,991 880,1011 423,1011" fill="var(--navy)"/>
      <polygon class="footer-banner" points="258,1011 880,1011 880,1101 258,1101 217,1056" fill="var(--orange)"/>
    </svg>

    <header class="brand">
      <div class="brand-dot"></div>
      <div class="brand-name">VANTORA GROUP</div>
    </header>

    <h1 class="banner-title">CORE VALUES</h1>

    <p class="intro">Our Core Values represent established principles that guide every action and decision of our organization.</p>

    <ul class="values">
      <li class="value value-integrity">
        <span class="value-name">INTEGRITY</span>
        <span class="value-text">Building trust through our honest and ethical business practices</span>
      </li>
      <li class="value value-dedication">
        <span class="value-name">DEDICATION</span>
        <span class="value-text">A relentless pursuit of excellence through partnership with our clients, consultants, and internal employees.</span>
      </li>
      <li class="value value-reliability">
        <span class="value-name">RELIABILITY</span>
        <span class="value-text">Taking responsibility at a consistently high level of performance through our expertise and commitment</span>
      </li>
      <li class="value value-value">
        <span class="value-name">VALUE</span>
        <span class="value-text">Through superior service-driven actions, we provide unparalleled value to our clients and consultants</span>
      </li>
      <li class="value value-unity">
        <span class="value-name">UNITY</span>
        <span class="value-text">Developing a team environment that thrives on healthy competition and personal growth.</span>
      </li>
    </ul>

    <footer class="web-address">WWW.VANTORAGROUP.COM</footer>
  </main>
</body>
</html>
```